KORAWIRE CAPABILITY STATEMENT “Building Tomorrow Today”

KORAWIRE CAPABILITY STATEMENT
“Building Tomorrow Today”
Indigenous-Owned Telecommunications & Infrastructure Solutions Partner

COVER PAGE

Visual: Modern and clean design featuring telecom towers, wind turbines, civil infrastructure, roads, and community WiFi imagery.
Tagline: “Connecting Communities, Powering Progress.”
Contact:
Website: www.korawire.com.au
Email: info@korawire.com.au
Phone: [Insert Main Number]
“Proudly Indigenous-Owned | Compliant with Aboriginal Procurement Policy (APP) & SME Policies”
INTRODUCTION

Korawire is a 100% Indigenous-owned leader in comprehensive infrastructure solutions, specializing in telecommunications, civil works, renewable energy, structural engineering, and site development. With over a decade of experience, we deliver safe, reliable, and culturally respectful services across Australia, from urban centers to remote wind farms and heritage sites. Our mission: “To bridge infrastructure gaps while empowering Indigenous communities and fostering sustainable growth.”

CORE CAPABILITIES

TELECOMMUNICATIONS

Tower Builds & Maintenance: Structural engineering, geotechnical analysis, foundation mapping.
Community WiFi Projects: Enhancing digital inclusion in Indigenous and remote communities.
Fiber & Wireless Networks: End-to-end installation for QLX, Satellite, and regional connectivity.
Height Safety Systems: Design, inspection, and certification of fall-arrest safety infrastructure.
CIVIL & STRUCTURAL ENGINEERING

Foundations & Concreting: Reinforced slabs, grillage, geotech-to-construction turnkey solutions.
Site Development: Earthworks, drainage, and access road/track construction.
Wind Farm Infrastructure: Reinforcing towers and integrating power systems for high-wind environments.
ROAD & ACCESS TRACK CONSTRUCTION

Construction of durable access roads and tracks: For remote projects and urban settings.
Remediation of existing tracks: Upgrading for environmental compliance and sustainability.
Facilitating logistics and site access: Particularly in challenging terrain.
POWER & ELECTRICAL SYSTEMS

Off-grid energy solutions: Solar hybrid systems, electrical structural engineering.
Grid upgrades: Ensuring compliance with AS/NZS standards and facilitating connection upgrades.
SITE REFURBISHMENT & DEMOLITION

Comprehensive refurbishment and demolition services: For outdated telecom sites and structures.
Environmentally responsible dismantling: Focused on recycling materials and minimizing land impact.
EMERGENCY RESPONSE SERVICES

24/7 Rapid Response: Over 450 callouts annually; 4,000+ emergencies resolved nationwide.
Disaster Recovery: Comprehensive support during floods, bushfires for QLX, Varnholt, Pellacast, and regional clients.
PROJECT EXPERIENCE

Heritage Tower Upgrade

Enhanced safety and technology on culturally significant heritage sites, preserving their integrity.
Wind Farm Deployment

Delivered power, fiber, and reinforced foundations for large-scale renewable energy projects in high-wind environments.
Regional Fibre Network

Laid 200km of fiber in flood-prone regions, ensuring critical infrastructure resilience.
Indigenous Community WiFi & Connectivity

Installed sustainable WiFi networks to bridge the digital divide, supporting education, health, and business activities.
Site Demolition & Refurbishment

Safely decommissioned aging telecom sites and structures across Australia, emphasizing land reuse and environmental care.
Access Track Construction & Remediation

Developed new access roads and refurbished existing tracks to facilitate project logistics, particularly in remote or environmentally sensitive areas.
Key Stats:
+600 sites supported | 10-year QLX partner | 98% client retention | Over 20 Indigenous community WiFi deployments

COMMITMENT TO SAFETY & QUALITY

“Pause and Check” Protocol: Enforced pre-task risk assessments to ensure safety at every stage.
Certifications: ISO 45001 (Safety) | ISO 9001 (Quality Management).
Safety Culture: Regular safety audits, Indigenous-led training programs, and safety initiatives focused on community well-being.
INDIGENOUS INCLUSION & COMMUNITY IMPACT

Elders Guidance Council: Provides guidance on community engagement, cultural sensitivity, and social responsibility.
Supplier Diversity: 30% procurement from Indigenous-owned businesses, fostering economic growth.
Regional Employment: 65% of our workforce originates from local communities, creating sustainable jobs.
Testimonial: “Korawire’s partnership empowered our community with jobs and infrastructure that respects our land.” – Local Indigenous Leader

CONTACT & SERVICE AREAS

Headquarters: [Insert Address] | ABN: [Insert ABN]

24/7 Emergency Support: [Insert Dedicated Emergency Line]

Certifications & Registrations:

Trade Circle Registered, Native Enterprise Register (NER)
SERVICE AREAS

National Coverage with Regional Expertise:
Major Cities: Sydney, Melbourne, Brisbane, Perth, Adelaide, Darwin, Hobart.
Regional & Remote Areas: Pilbara, Kimberley, Far North Queensland, Outback NSW.
Disaster Zones: Rapid response teams deployed nationwide for bushfire and flood incidents.
EMERGENCY SUPPORT

SLA Guarantee: 90% of emergencies addressed within 4 hours.
Partners Supported: QLX, Varnholt, Pellacast, regional councils.
This capability statement reflects our commitment to quality, safety, and community engagement across all levels of operation, ensuring that we empower the communities we serve while maintaining the highest standards of service delivery.

Target Market(s)

Government Agencies: Especially those seeking to comply with Indigenous Procurement Policies. Telecommunication Operators: Such as QLX, Varnholt, and Pellacast for infrastructure deployment. Indigenous Communities: Projects aimed at enhancing connectivity and digital inclusion. Utilities and Energy Providers: For power and electrical infrastructure projects. Construction and Engineering Firms: Seeking collaboration on civil and structural infrastructure projects.

Industry/Entity Type

Telecommunications and Infrastructure Development: Focused on service delivery in various contexts, including urban settings, remote locations, and Indigenous community projects. Renewable Energy: This includes wind and solar infrastructure linked to telecommunications enhancements. Civil Engineering: Related to building and maintaining essential infrastructure such as access roads and utility lines.

Font styles to use
Other font styles liked:
• Bubbleboddy neue

Requirements
Must have
• Clear demonstration of Indigenous ownership and community engagement. Compliance with relevant safety and quality certifications (e.g., ISO 45001, ISO 9001). Showcase of core capabilities in telecommunications, civil engineering, and those specific to renewable energy. Visuals that reflect the diverse range of services offered (like telecom towers and community WiFi installations).
Nice to have
• Interactive elements such as hyperlinks to project case studies or client testimonials. Infographics or visual data to highlight key statistics and project success rates. Cultural motifs or imagery that reflect Indigenous heritage and inclusion in design aspirations. QR codes that link to videos or more detailed project descriptions for digital formats.
Should not have
• Clutter or excessive text that detracts from the main messages. Generic stock images that don’t align with the specific projects or Indigenous culture. Technical jargon that could confuse stakeholders unfamiliar with industry-specific terms. Overemphasis on competitors; the focus should remain on Korawire's unique strengths and contributions.

```html
<!DOCTYPE html>
<html lang="en">
<head>
<meta charset="utf-8">
<title>Korawire Capability Statement – Introduction &amp; Core Capabilities</title>
<link href="https://fonts.googleapis.com/css2?family=Montserrat:wght@300;400;500;600;700;800&display=swap" rel="stylesheet">
<style>
  :root {
    --brand-red: #a0101c;
    --brand-red-dark: #7d0a14;
    --ink: #1b1b1b;
    --body-grey: #555555;
    --row-grey: #f3f3f3;
    --rule-grey: #c9c9c9;
    --paper: #ffffff;
  }
  * { box-sizing: border-box; margin: 0; padding: 0; }
  html, body { width: 1200px; height: 777px; overflow: hidden; background: var(--paper); }
  body { font-family: "Montserrat", Arial, sans-serif; color: var(--ink); }
  .spread { position: relative; width: 1200px; height: 777px; }

  .section-title {
    position: absolute; left: 45px; top: 44px;
    font-size: 15px; font-weight: 800; letter-spacing: .2px;
    padding-left: 9px; border-left: 5px solid var(--brand-red); line-height: 14px;
  }
  .split-title {
    position: absolute; padding-left: 10px; border-left: 5px solid var(--brand-red);
    font-size: 15px; line-height: 16px;
  }
  .split-title .light { display: block; font-weight: 400; }
  .split-title .bold { display: block; font-weight: 700; }

  .body-copy {
    position: absolute; left: 45px; width: 510px;
    font-size: 11px; line-height: 17.6px; color: var(--body-grey);
    text-align: justify; font-weight: 400;
  }

  .frame-corner { position: absolute; background: var(--brand-red); }
  .team-photo {
    position: absolute; left: 55px; top: 280px; width: 491px; height: 256px;
    background: linear-gradient(180deg, #6f7a8c 0%, #5a6b4a 35%, #3c3a34 70%, #d9d9d6 100%);
  }

  .page-footer { position: absolute; top: 724px; height: 14px; }
  .footer-brand { position: absolute; left: 0; top: 0; font-size: 9.5px; font-weight: 600; color: var(--brand-red); line-height: 14px; letter-spacing: .2px; white-space: nowrap; }
  .footer-rule { position: absolute; top: 7px; height: 1px; background: var(--rule-grey); }
  .footer-rule-accent { position: absolute; top: 6px; height: 2px; width: 37px; background: var(--ink); }
  .page-number {
    position: absolute; top: 0; width: 14px; height: 14px; background: var(--brand-red);
    color: #fff; font-size: 9px; font-weight: 700; text-align: center; line-height: 14px;
  }

  .group-heading {
    position: absolute; left: 644px; font-size: 13.5px; font-weight: 700;
    color: var(--brand-red); letter-spacing: .2px;
  }
  .cap-row { position: absolute; left: 644px; width: 511px; height: 33px; background: var(--row-grey); }
  .cap-label {
    position: absolute; left: 0; top: 0; width: 125px; height: 33px;
    background: linear-gradient(90deg, var(--brand-red) 80%, var(--brand-red-dark) 100%);
    clip-path: polygon(0 0, 110px 0, 125px 50%, 110px 100%, 0 100%);
    color: #fff; font-size: 11px; font-weight: 600; line-height: 13px;
    padding-left: 8px; display: flex; align-items: center; white-space: nowrap;
  }
  .cap-label.tight { font-size: 10px; }
  .cap-desc {
    position: absolute; left: 131px; right: 4px; top: 0; height: 33px;
    display: flex; align-items: center;
    font-size: 10.2px; line-height: 13px; color: var(--ink); font-weight: 400;
  }
</style>
</head>
<body>
<main class="spread">

  <section class="page page-intro">
    <h2 class="section-title">INTRODUCTION</h2>

    <p class="body-copy" style="top:78px;">Kora Service Group unites Korawire, KoraCivil, and KoraElectrical to provide a complete, end-to-end service offering. Our capabilities cover tower erection, fibre deployment, labour resourcing, data and electrical works, asset maintenance, and satellite support — delivering integrated solutions across the telecommunications and infrastructure sectors.</p>

    <p class="body-copy" style="top:166px;">Headquartered in Eastern Australia, we also deliver projects nationally. As a 100% Indigenous-owned company, we are committed to combining technical expertise with a culturally respectful approach. We work in partnership with communities to ensure every project supports local engagement, creates opportunities, and respects Country.</p>

    <div class="frame-corner" style="left:45px; top:270px; width:105px; height:10px;"></div>
    <div class="frame-corner" style="left:45px; top:270px; width:10px; height:64px;"></div>
    <div class="team-photo" role="img" aria-label="Photo of three team members in black hats in front of a telecom tower and rolling farmland"></div>
    <div class="frame-corner" style="left:546px; top:482px; width:9px; height:63px;"></div>
    <div class="frame-corner" style="left:450px; top:536px; width:105px; height:9px;"></div>

    <h2 class="split-title" style="left:45px; top:578px;">
      <span class="light">Our</span>
      <span class="bold">Mission</span>
    </h2>
    <p class="body-copy" style="top:630px;">To bridge infrastructure gaps while empowering Indigenous communities and fostering sustainable growth.</p>

    <footer class="page-footer" style="left:45px; width:510px;">
      <span class="footer-brand">KORAWIRE</span>
      <span class="footer-rule" style="left:64px; width:432px;"></span>
      <span class="footer-rule-accent" style="left:64px;"></span>
      <span class="page-number" style="left:496px;">2</span>
    </footer>
  </section>

  <section class="page page-capabilities">
    <h2 class="split-title" style="left:644px; top:44px;">
      <span class="light">CORE</span>
      <span class="bold">CAPABILITIES</span>
    </h2>

    <h3 class="group-heading" style="top:96px;">TELECOMMUNICATIONS</h3>
    <div class="cap-row" style="top:121px;"><div class="cap-label"><span>Tower Builds &amp;<br>Maintenance:</span></div><p class="cap-desc">Structural engineering, geotechnical analysis, foundation mapping.</p></div>
    <div class="cap-row" style="top:163px;"><div class="cap-label"><span>Community WiFi<br>Projects:</span></div><p class="cap-desc">Enhancing digital inclusion in Indigenous and remote communities.</p></div>
    <div class="cap-row" style="top:206px;"><div class="cap-label"><span>Fiber &amp; Wireless<br>Networks:</span></div><p class="cap-desc">End-to-end installation for QLX, Satellite, and regional connectivity.</p></div>
    <div class="cap-row" style="top:248px;"><div class="cap-label"><span>Height Safety<br>Systems:</span></div><p class="cap-desc">Design, inspection, and certification of fall-arrest safety infrastructure.</p></div>

    <h3 class="group-heading" style="top:301px;">CIVIL &amp; STRUCTURAL ENGINEERING</h3>
    <div class="cap-row" style="top:323px;"><div class="cap-label"><span>Foundations &amp;<br>Concreting:</span></div><p class="cap-desc">Reinforced slabs, grillage, geotech-to-construction turnkey solutions.</p></div>
    <div class="cap-row" style="top:365px;"><div class="cap-label"><span>Site<br>Development:</span></div><p class="cap-desc">Earthworks, drainage, and access road/track construction.</p></div>
    <div class="cap-row" style="top:407px;"><div class="cap-label"><span>Wind Farm<br>Infrastructure:</span></div><p class="cap-desc">Reinforcing towers and integrating power systems for high-wind environments.</p></div>

    <h3 class="group-heading" style="top:461px;">ROAD &amp; ACCESS TRACK CONSTRUCTION</h3>
    <div class="cap-row" style="top:484px;"><div class="cap-label"><span>Constructions<br>Durability</span></div><p class="cap-desc">Construction of durable access roads and tracks - For remote projects and urban settings.</p></div>
    <div class="cap-row" style="top:527px;"><div class="cap-label"><span>Remediation of<br>existing tracks:</span></div><p class="cap-desc">&nbsp;Upgrading for environmental compliance and sustainability.</p></div>
    <div class="cap-row" style="top:569px;"><div class="cap-label tight"><span>Facilitating logistics<br>&amp; site access</span></div><p class="cap-desc">Particularly in challenging terrain.</p></div>

    <h3 class="group-heading" style="top:623px;">POWER &amp; ELECTRICAL SYSTEMS</h3>
    <div class="cap-row" style="top:644px;"><div class="cap-label"><span>Off-grid Energy<br>Solutions:</span></div><p class="cap-desc">Solar hybrid systems, electrical structural engineering.</p></div>
    <div class="cap-row" style="top:686px;"><div class="cap-label"><span>Grid Upgrades:</span></div><p class="cap-desc">Ensuring compliance with AS/NZS standards and facilitating connection upgrades.</p></div>

    <footer class="page-footer" style="left:644px; width:511px;">
      <span class="footer-brand">KORAWIRE</span>
      <span class="footer-rule" style="left:64px; width:433px;"></span>
      <span class="footer-rule-accent" style="left:64px;"></span>
      <span class="page-number" style="left:497px;">3</span>
    </footer>
  </section>

</main>
</body>
</html>
```